Company director needs a business card design

I am a semi-retired former senior finance executive who sits on a number of public and private company boards and do some consulting work. I work largely with emerging businesses but deal regularly with top end of town lawyers, bankers etc. I need a thoughtful but relatively conservative design which would also resonate with my younger client base. Some colour would be good. Information limited to name, address, office tel, mobile and email.

Industry/Entity Type

Finance

```html
<!DOCTYPE html>
<html lang="en">
<head>
<meta charset="utf-8">
<title>Martin Ellwood — Business Card</title>
<link href="https://fonts.googleapis.com/css2?family=Cinzel:wght@400;700&display=swap" rel="stylesheet">
<style>
  :root {
    --backdrop: #e6e6e6;
    --card-light: #f5f5f4;
    --card-dark: #262627;
    --ink-name-light: #5a5a5a;
    --ink-detail-light: #8c8c8c;
    --ink-name-dark: #7a7a7a;
    --ink-detail-dark: #646464;
  }
  html, body {
    margin: 0;
    padding: 0;
    width: 1200px;
    height: 720px;
    overflow: hidden;
    background: var(--backdrop);
  }
  .canvas {
    position: relative;
    width: 1200px;
    height: 720px;
  }
  .card {
    position: absolute;
    top: 242px;
    width: 420px;
    height: 238px;
    box-sizing: border-box;
    padding: 114px 0 0 34px;
    font-family: "Cinzel", serif;
  }
  .card--light { left: 147px; background: var(--card-light); }
  .card--dark  { left: 633px; background: var(--card-dark); }

  .card__name {
    margin: 0;
    font-size: 14px;
    font-weight: 700;
    letter-spacing: 0.02em;
    line-height: 18px;
  }
  .card__address {
    margin: 13px 0 0;
    font-size: 10.5px;
    line-height: 13px;
  }
  .card__contacts {
    margin: 13px 0 0;
    padding: 0;
    list-style: none;
    font-size: 10.5px;
    line-height: 12.5px;
  }
  .card--light .card__name { color: var(--ink-name-light); }
  .card--light .card__address,
  .card--light .card__contacts { color: var(--ink-detail-light); }
  .card--dark .card__name { color: var(--ink-name-dark); }
  .card--dark .card__address,
  .card--dark .card__contacts { color: var(--ink-detail-dark); }
</style>
</head>
<body>
<main class="canvas">
  <section class="card card--light" aria-label="Business card, light version">
    <h1 class="card__name">Martin Ellwood</h1>
    <p class="card__address">18 Larkspur Street, Balmoral NSW 2088</p>
    <ul class="card__contacts">
      <li>02 9000 4812</li>
      <li>0400 555 218</li>
      <li>martin_ellwood@oaknet.net.au</li>
    </ul>
  </section>

  <section class="card card--dark" aria-label="Business card, dark version">
    <h2 class="card__name">Martin Ellwood</h2>
    <p class="card__address">18 Larkspur Street, Balmoral NSW 2088</p>
    <ul class="card__contacts">
      <li>02 9000 4812</li>
      <li>0400 555 218</li>
      <li>martin_ellwood@oaknet.net.au</li>
    </ul>
  </section>
</main>
</body>
</html>
```